Customer Dashboard Design for Email Security SaaS

Mailvarden is a commercial email spam filter offered as a SaaS product, built and operated by a small German hosting provider. It protects business email accounts against spam, phishing, scam, and viruses using a multilayer filtering pipeline that combines traditional spam detection with AI-powered classification. The product runs entirely on German infrastructure, ensuring data sovereignty for European customers.

We need a complete redesign of the customer-facing dashboard. This is the web application where paying customers manage their email filtering: view their mail log, check quarantined emails, manage allow/blocklists, configure their settings, and handle their subscription. It is the primary touchpoint between Mailvarden and its customers.

Our customers are system administrators, IT managers at small-to-medium businesses, and operators of small hosting providers. They are technically competent but not designers. They expect professional, efficient tools that respect their time. They typically manage 10–500 email accounts and check the dashboard a few times per week, with heavier use during spam incidents.

We have attached the current mockups which really need to be replaced with something good looking.

Target Market(s)

System administrators, IT managers at small-to-medium businesses, and operators of small hosting providers.

Industry/Entity Type

SaaS

Number of Pages Required

5+ page

```html
<!DOCTYPE html>
<html lang="en">
<head>
<meta charset="utf-8">
<title>Mailvarden Dashboard</title>
<link rel="stylesheet" href="https://fonts.googleapis.com/css2?family=Inter:wght@400;500;600;700;800&family=IBM+Plex+Mono:wght@400;500;600&display=swap">
<style>
:root{
  --bg:#1a1917;
  --header:#141311;
  --sidebar:#1c1b19;
  --card:#232220;
  --chip:#2c2b28;
  --accent:#e8a84c;
  --accent-text:#f0a640;
  --bar:#9a7540;
  --text:#f5f3ef;
  --muted:#cfcbc4;
  --line:#3a3833;
}
*{box-sizing:border-box;margin:0;padding:0}
html,body{width:1200px;height:1064px;overflow:hidden;background:var(--bg)}
body{position:relative;font-family:"Inter",sans-serif;color:var(--text)}
.mono{font-family:"IBM Plex Mono",monospace}
.abs{position:absolute}

.topbar{position:absolute;left:0;top:0;width:1200px;height:80px;background:var(--header);border-bottom:1px solid #242320}
.brand{left:20px;top:22px;font-size:27px;font-weight:500;letter-spacing:-0.5px}
.nav a{position:absolute;top:33px;font-size:11px;font-weight:500;color:var(--text);text-decoration:none;letter-spacing:.3px}
.nav a.active{color:var(--accent-text);border-bottom:2px solid var(--accent);padding-bottom:3px}
.icon-btn{position:absolute;top:30px;width:20px;height:20px}
.sys-check{left:892px;top:20px;width:111px;height:40px;background:#2b2a27;border-radius:6px;font-size:12px;display:flex;align-items:center;justify-content:center;color:var(--muted)}
.user{left:1053px;top:31px;font-size:14px;font-weight:500}
.avatar{left:1130px;top:20px;width:40px;height:40px;border:1px solid #6a6760;border-radius:50%}

.sidebar{position:absolute;left:0;top:80px;width:197px;height:984px;background:var(--sidebar)}
.side-item{position:absolute;left:32px;display:flex;align-items:center;gap:10px;font-size:12px;color:var(--text)}
.side-item svg{width:16px;height:16px;flex:none}
.side-item.active{color:var(--accent-text);font-size:13px}
.active-mark{left:173px;top:127px;width:5px;height:40px;border-right:1.5px solid var(--accent);border-radius:0 6px 6px 0}
.divider{left:18px;top:543px;width:159px;height:1px;background:var(--line)}
.admin-label{left:20px;top:568px;font-size:10px;font-weight:500}
.audit{left:19px;top:680px;width:158px;height:40px;background:var(--accent);border-radius:6px;color:#1a1917;font-size:13px;font-weight:600;display:flex;align-items:center;justify-content:center}

.greeting{left:217px;top:124px;font-size:40px;font-weight:800;letter-spacing:-0.5px}
.sub{left:217px;top:188px;font-size:15px;color:var(--muted)}
.action{position:absolute;top:263px;height:40px;background:#2b2a27;border-radius:6px;display:flex;align-items:center;gap:10px;padding-left:15px;font-size:12px;color:var(--muted)}
.action svg{width:17px;height:17px}
.action.outline{background:transparent;border:1px solid var(--accent);color:var(--accent-text)}

.card{position:absolute;background:var(--card);border-radius:16px}
.total{left:217px;top:323px;width:766px;height:195px}
.total .label{position:absolute;left:30px;top:38px;font-size:12px;font-weight:600;letter-spacing:2.5px;color:var(--accent-text)}
.total .value{position:absolute;left:28px;top:60px;font-size:55px;font-weight:700;letter-spacing:-1px}
.total .desc{position:absolute;left:30px;top:143px;font-size:14px;font-weight:500;color:var(--muted)}

.threats{position:absolute;left:217px;top:538px;width:766px;height:100px;border-radius:16px;background:linear-gradient(90deg,#2a2620 0%,#6b5230 45%,#e8a84c 100%)}
.threats .big{position:absolute;left:30px;top:22px;font-size:30px;font-weight:700}
.threats .small{position:absolute;left:30px;top:63px;font-size:13px;color:var(--muted)}
.threats .status{position:absolute;left:512px;top:32px;font-size:13px;line-height:18px;color:#1e1c18}

.chart{left:217px;top:662px;width:769px;height:382px}
.chart h2{position:absolute;left:33px;top:32px;font-size:42px;font-weight:700;letter-spacing:-0.3px}
.chart .csub{position:absolute;left:33px;top:91px;font-size:13px;color:var(--muted)}
.chip{position:absolute;top:129px;height:26px;border-radius:6px;background:#1b1a18;font-size:12px;display:flex;align-items:center;justify-content:center}
.chip.on{background:var(--accent);color:#1a1917}
.bars{position:absolute;left:33px;top:191px}
.axis{position:absolute;top:345px;font-size:8px}

.stat{position:absolute;left:1003px;width:177px;height:177px;background:var(--card);border-radius:16px}
.badge{position:absolute;right:14px;top:16px;height:22px;padding:0 8px;background:#2d2b28;border-radius:5px;font-size:11px;color:#f08a2c;display:flex;align-items:center}
.stat .ico{position:absolute;left:20px;top:50px;width:40px;height:40px;border-radius:50%;background:#181715;display:flex;align-items:center;justify-content:center}
.stat .ico svg{width:18px;height:18px}
.stat .name{position:absolute;left:20px;top:103px;font-size:14px;color:var(--muted)}
.stat .num{position:absolute;left:20px;top:124px;font-size:25px;font-weight:500}
</style>
</head>
<body>

<header class="topbar">
  <div class="abs brand">Mailvarden</div>
  <nav class="nav">
    <a class="active" style="left:233px" href="#">DASHBOARD</a>
    <a style="left:335px" href="#">ANALYTICS</a>
    <a style="left:427px" href="#">REPORTS</a>
  </nav>
  <svg class="icon-btn" style="left:800px" viewBox="0 0 24 24" fill="none" stroke="#f5f3ef" stroke-width="1.8"><path d="M6 17V11a6 6 0 0 1 12 0v6l2 2H4z"/><path d="M10 21h4"/><path d="M3 6l2-2M21 6l-2-2"/></svg>
  <svg class="icon-btn" style="left:840px" viewBox="0 0 24 24" fill="none" stroke="#f5f3ef" stroke-width="1.8"><circle cx="12" cy="12" r="3"/><path d="M12 2l2 3 3.5-.8.8 3.5 3 2-2 3 .8 3.5-3.5.8-2 3-3-2-3 2-2-3-3.5-.8.8-3.5-2-3 3-2 .8-3.5L10 5z"/></svg>
  <div class="abs sys-check mono">System Check</div>
  <div class="abs user">Admin_02</div>
  <svg class="abs avatar" viewBox="0 0 40 40"><circle cx="20" cy="15" r="6" fill="#8a867e"/><path d="M9 30a11 8 0 0 1 22 0z" fill="#8a867e"/></svg>
</header>

<aside class="sidebar">
  <div class="abs active-mark" style="top:47px"></div>
  <div class="side-item active mono" style="top:59px">
    <svg viewBox="0 0 24 24" fill="none" stroke="#e8a84c" stroke-width="2"><path d="M4 11l8-7 8 7v9H4z"/><path d="M10 20v-5h4v5"/></svg>OVERVIEW</div>
  <div class="side-item mono" style="top:110px">
    <svg viewBox="0 0 24 24" fill="none" stroke="#f5f3ef" stroke-width="1.8"><rect x="3" y="5" width="18" height="14"/><path d="M3 9h18M6 15h12"/></svg>Mail-Log</div>
  <div class="side-item mono" style="top:162px">
    <svg viewBox="0 0 24 24" fill="none" stroke="#f5f3ef" stroke-width="1.8"><path d="M3 9l9-5 9 5v11H3z"/><path d="M3 9l9 6 9-6"/></svg>MAILBOX</div>
  <div class="side-item mono" style="top:214px">
    <svg viewBox="0 0 24 24" fill="none" stroke="#f5f3ef" stroke-width="1.8"><path d="M12 3l8 3v6c0 5-4 8-8 9-4-1-8-4-8-9V6z"/><path d="M8.5 12l2.5 2.5 4.5-5"/></svg>Allowlist</div>
  <div class="side-item mono" style="top:265px">
    <svg viewBox="0 0 24 24" fill="none" stroke="#f5f3ef" stroke-width="1.8"><path d="M12 3l8 3v6c0 5-4 8-8 9-4-1-8-4-8-9V6z"/><path d="M12 8v5M12 16v.5"/></svg>Blocklist</div>
  <div class="side-item mono" style="top:317px">
    <svg viewBox="0 0 24 24" fill="none" stroke="#f5f3ef" stroke-width="1.8"><rect x="5" y="10" width="14" height="11" rx="1"/><path d="M8 10V7a4 4 0 0 1 8 0v3"/><circle cx="12" cy="15.5" r="1.2"/></svg>Quarantane</div>
  <div class="side-item mono" style="top:369px">
    <svg viewBox="0 0 24 24" fill="none" stroke="#f5f3ef" stroke-width="1.8"><circle cx="12" cy="12" r="3"/><path d="M12 2l2 3 3.5-.8.8 3.5 3 2-2 3 .8 3.5-3.5.8-2 3-3-2-3 2-2-3-3.5-.8.8-3.5-2-3 3-2 .8-3.5L10 5z"/></svg>SETTINGS</div>
  <div class="side-item mono" style="top:420px">
    <svg viewBox="0 0 24 24" fill="none" stroke="#f5f3ef" stroke-width="1.8"><rect x="4" y="7" width="17" height="11"/><path d="M2 9v11h16"/><circle cx="12.5" cy="12.5" r="2.5"/></svg>BILLING</div>
  <div class="abs divider" style="top:463px"></div>
  <div class="abs admin-label" style="top:488px">ADMINISTRATION</div>
  <div class="side-item mono" style="top:528px;left:30px">System Settings</div>
  <div class="abs audit mono" style="top:600px">Security Audit</div>
  <div class="side-item mono" style="top:674px;left:20px">
    <svg viewBox="0 0 24 24" fill="none" stroke="#f5f3ef" stroke-width="1.8"><circle cx="12" cy="12" r="9"/><path d="M9.5 9.5a2.5 2.5 0 1 1 3.5 2.3c-.8.4-1 1-1 1.7M12 16.5v.5"/></svg>Help Center</div>
  <div class="side-item mono" style="top:715px;left:20px">
    <svg viewBox="0 0 24 24" fill="none" stroke="#f5f3ef" stroke-width="1.8"><path d="M10 4H4v16h6"/><path d="M10 12h10M16 8l4 4-4 4"/></svg>Log Out</div>
</aside>

<main>
  <h1 class="abs greeting">Good morning, Administrator</h1>
  <p class="abs sub">Your email security system is running smoothly.</p>

  <div class="action mono" style="left:217px;width:160px">
    <svg viewBox="0 0 24 24" fill="none" stroke="#f5f3ef" stroke-width="1.8"><rect x="3" y="4" width="18" height="5"/><path d="M5 9v11h14V9M10 13h4"/></svg>View Quarantine</div>
  <div class="action mono" style="left:397px;width:146px">
    <svg viewBox="0 0 24 24" fill="none" stroke="#f5f3ef" stroke-width="1.8"><path d="M3 6h18v13H3z"/><path d="M3 6l9 7 9-7"/><path d="M9 15l2 2 4-4"/></svg>Open Mail Log</div>
  <div class="action mono" style="left:563px;width:154px">
    <svg viewBox="0 0 24 24" fill="none" stroke="#f5f3ef" stroke-width="1.8"><path d="M4 4h16M12 20V8M7 13l5-5 5 5"/></svg>Release Emails</div>
  <div class="action outline mono" style="left:837px;width:146px">
    <svg viewBox="0 0 24 24" fill="none" stroke="#e8a84c" stroke-width="1.8"><path d="M3 6h18M3 12h18M3 18h18"/><path d="M8 4v4M15 10v4M10 16v4"/></svg>Adjust Filter</div>

  <section class="card total">
    <div class="label">TOTAL EMAILS PROTECTED</div>
    <div class="value">2,153,142</div>
    <div class="desc">Emails secured in the last 30 days &nbsp;&nbsp;&nbsp;·&nbsp;&nbsp;&nbsp; +12.4% improvement from previous period</div>
  </section>

  <section class="threats">
    <div class="big">4 threats</div>
    <div class="small mono">mitigated in the last hour.</div>
    <div class="status mono">All protection layers are<br>operating normally</div>
  </section>

  <section class="card chart">
    <h2>Security Traffic Analysis</h2>
    <p class="csub">Email filtering trends across the last 30 days</p>
    <div class="chip on mono" style="left:33px;width:38px">All</div>
    <div class="chip mono" style="left:95px;width:45px">Spam</div>
    <div class="chip mono" style="left:165px;width:72px">Phishing</div>
    <div class="chip mono" style="left:262px;width:52px">Virus</div>
    <div class="chip mono" style="left:338px;width:94px">Newsletters</div>
    <svg class="bars" width="603" height="149" viewBox="0 0 724 178" role="img" aria-label="Daily filtered email volume, last 30 days">
      <g fill="var(--bar)">
        <rect x="0" y="61" width="24" height="117"/>
        <rect x="28" y="26" width="24" height="152"/>
        <rect x="56" y="0" width="24" height="178"/>
        <rect x="84" y="44" width="24" height="134"/>
        <rect x="112" y="101" width="24" height="77"/>
        <rect x="140" y="35" width="24" height="143"/>
        <rect x="168" y="44" width="24" height="134"/>
        <rect x="196" y="61" width="24" height="117"/>
        <rect x="224" y="26" width="24" height="152"/>
        <rect x="252" y="61" width="24" height="117"/>
        <rect x="280" y="46" width="24" height="132"/>
        <rect x="308" y="61" width="24" height="117"/>
        <rect x="336" y="0" width="24" height="178"/>
        <rect x="364" y="15" width="24" height="163"/>
        <rect x="392" y="79" width="24" height="99"/>
        <rect x="420" y="44" width="24" height="134"/>
        <rect x="448" y="26" width="24" height="152"/>
        <rect x="476" y="7" width="24" height="171"/>
        <rect x="504" y="72" width="24" height="106"/>
        <rect x="532" y="94" width="24" height="84"/>
        <rect x="560" y="79" width="24" height="99"/>
        <rect x="588" y="35" width="24" height="143"/>
        <rect x="616" y="72" width="24" height="106"/>
        <rect x="644" y="46" width="24" height="132"/>
        <rect x="672" y="94" width="24" height="84"/>
        <rect x="700" y="79" width="24" height="99"/>
      </g>
    </svg>
    <div class="axis mono" style="left:33px">30 Days Ago</div>
    <div class="axis mono" style="left:612px">Today</div>
  </section>

  <section class="stat" style="top:100px">
    <div class="badge mono">+8% increase</div>
    <div class="ico"><svg viewBox="0 0 24 24" fill="none" stroke="#f5f3ef" stroke-width="1.8"><circle cx="12" cy="12" r="8"/><path d="M6.5 6.5l11 11"/></svg></div>
    <div class="name">Spam Blocked</div>
    <div class="num">842,109</div>
  </section>
  <section class="stat" style="top:298px">
    <div class="badge mono">+2% increase</div>
    <div class="ico"><svg viewBox="0 0 24 24" fill="none" stroke="#f5f3ef" stroke-width="1.8"><path d="M14 3v10a4 4 0 0 1-8 0v-2l2 2"/></svg></div>
    <div class="name">Phishing Detected</div>
    <div class="num">12,402</div>
  </section>
  <section class="stat" style="top:497px">
    <div class="badge mono">-5% decrease</div>
    <div class="ico"><svg viewBox="0 0 24 24" fill="none" stroke="#f5f3ef" stroke-width="1.8"><circle cx="12" cy="12" r="5"/><path d="M12 3v4M12 17v4M3 12h4M17 12h4M5.6 5.6l2.9 2.9M15.5 15.5l2.9 2.9M5.6 18.4l2.9-2.9M15.5 8.5l2.9-2.9"/></svg></div>
    <div class="name">Viruses Caught</div>
    <div class="num">3,891</div>
  </section>
  <section class="stat" style="top:695px">
    <div class="badge mono">+14% increase</div>
    <div class="ico"><svg viewBox="0 0 24 24" fill="none" stroke="#f5f3ef" stroke-width="1.8"><path d="M6 3h12M6 21h12M7 3c0 5 5 6 5 9s-5 4-5 9M17 3c0 5-5 6-5 9s5 4 5 9"/></svg></div>
    <div class="name" style="left:24px">In Quarantine</div>
    <div class="num">776</div>
  </section>
  <section class="stat" style="top:893px">
    <div class="badge mono">0% change</div>
    <div class="ico"><svg viewBox="0 0 24 24" fill="none" stroke="#f5f3ef" stroke-width="1.8"><rect x="3" y="6" width="18" height="13"/><path d="M3 6l9 7 9-7"/></svg></div>
    <div class="name">Newsletters Sorted</div>
    <div class="num">390,214</div>
  </section>
</main>

</body>
</html>
```